Brand and Marketing Coach Needs PDF Designed

I have content that i need placed into a simple but great PDF design. The PDF is about the formula I use to build personal brands. This is geared towards entrepreneurs, experts, coaches, therapists, wellness practitioners, and indpendent business owners who serve to improve the lives of others.
The company name is changing from BrovelStudio to Branding with the Crowd (I don't have that logo yet, so working backwards a bit. For now, the BrovelStudio logo can be used.) My brand is NOT formal and corporate, but it's also not neon-pink and screaming at you. It's down to earth, hip, a bit modern but warm. It's about no BS and authenticity. The final deliverable should make the reader feel focused, smart, motivated and hopeful.

Target Market(s)

Conscious entrepreneurs and small business owners. this one is specifically for pharmacy entrepreneurs but this will be used for various audiences later.

Font styles to use
Sans Serif

Colors
eaf1f7
3377b5
6b449b
f37122
faa54b
f68e4e
ffc214

Requirements
Must have
• Modern design. colors that match logo - 4e5583 (i think that is the blue.) d65a40.
• Could have these colors as well: c6a254, 01bcc3
• But open to other colors
Nice to have
• I'd like to see some ways to make this PDF simple and readable, and eye-catching. I'd also like to use the uploaded ebooks for design ideas.
Should not have
• neon colors, clip art

```html
<!DOCTYPE html>
<html lang="en">
<head>
<meta charset="utf-8">
<title>Solo Signal Method – Workbook Spreads</title>
<link href="https://fonts.googleapis.com/css2?family=EB+Garamond:ital,wght@0,400;0,500;0,600;1,400&family=Playfair+Display:ital,wght@0,400;1,400&display=swap" rel="stylesheet">
<style>
  :root {
    --canvas: #ffffff;
    --page: #4f5683;
    --cell-dark: #363a5c;
    --field: #ffffff;
    --ink-light: #ffffff;
    --ink-soft: #e8eaf3;
    --rule: #4f5683;
  }
  * { box-sizing: border-box; margin: 0; padding: 0; }
  html, body { width: 1200px; height: 957px; overflow: hidden; background: var(--canvas); }
  body { position: relative; font-family: "EB Garamond", Georgia, serif; color: var(--ink-light); }

  .page { position: absolute; width: 544px; height: 421px; background: var(--page); }
  .page--value-intro   { left: 45px;  top: 37px; }
  .page--value-summary { left: 611px; top: 37px; }
  .page--client-intro  { left: 45px;  top: 483px; }
  .page--client-detail { left: 611px; top: 483px; }

  .abs { position: absolute; }

  .section-badge {
    position: absolute; left: 50px; top: 45px; width: 32px; height: 32px;
    border-radius: 50%; background: var(--field); color: var(--page);
    font-family: "Playfair Display", Georgia, serif; font-style: italic;
    font-size: 22px; line-height: 32px; text-align: center;
  }
  .section-title {
    position: absolute; left: 94px; top: 45px; line-height: 32px;
    font-family: "Playfair Display", Georgia, serif; font-size: 22px; font-weight: 400;
  }
  .lead {
    position: absolute; left: 50px; width: 444px;
    font-size: 13.5px; font-weight: 500; line-height: 15px;
  }
  .body-copy {
    position: absolute; left: 50px; width: 444px;
    font-size: 9.6px; line-height: 11.6px; color: var(--ink-soft);
  }
  .prompt {
    position: absolute; left: 50px; width: 444px;
    font-size: 9.2px; line-height: 11.4px; font-style: italic; color: var(--ink-soft);
  }
  .prompt .upright { font-style: normal; }
  .field { position: absolute; left: 50px; width: 442px; background: var(--field); }
  .subhead {
    position: absolute; left: 50px; font-size: 12.5px; font-weight: 600; line-height: 14px;
  }
  .folio {
    position: absolute; left: 0; right: 0; top: 384px; text-align: center;
    font-size: 6px; letter-spacing: .04em; color: var(--ink-soft);
  }

  .profile-table {
    position: absolute; left: 50px; width: 442px;
    display: grid; grid-template-columns: 187px 127px 128px;
  }
  .profile-table .head {
    background: var(--cell-dark); text-transform: uppercase; letter-spacing: .05em;
    font-size: 10px; display: flex; align-items: center; justify-content: center;
    border-left: 1px solid var(--rule);
  }
  .profile-table .blank { background: transparent; }
  .profile-table .label {
    background: var(--cell-dark); font-size: 9.6px; line-height: 10px;
    display: flex; flex-direction: column; align-items: flex-end; justify-content: center;
    padding-right: 8px; text-align: right; border-top: 1px solid var(--rule);
  }
  .profile-table .cell {
    background: var(--field); border-top: 1px solid var(--rule); border-left: 1px solid var(--rule);
  }

  .word-boxes { position: absolute; left: 50px; top: 313px; display: flex; gap: 5px; }
  .word-boxes span { display: block; width: 144px; height: 44px; background: var(--field); }
</style>
</head>
<body>

<section class="page page--value-intro">
  <div class="section-badge">2</div>
  <h2 class="section-title">VALUE</h2>
  <p class="lead" style="top:93px">Your expertise and the results your clients get from working with you.</p>
  <p class="body-copy" style="top:107px">Your prospects must understand what you do and what you’re asking them to do. As time and attention span continue to decrease, people just won’t stick around long enough to research how you can help them. To succinctly communicate your value, you must know simplify who you are, what you do, and how you do it into a clear value statement. Getting this right means you also have a great bit of content already written for your website.</p>
  <p class="prompt" style="top:182px">What is your expertise – what do you consider yourself to be the authority on?</p>
  <div class="field" style="top:198px;height:42px"></div>
  <p class="prompt" style="top:261px">How do you do this in a way that is different from others in your industry? Is there something about how you work with customers to get them results, that is different from how others in your industry may do this?</p>
  <div class="field" style="top:288px;height:78px"></div>
  <p class="folio">PAGE X OF XX</p>
</section>

<section class="page page--value-summary">
  <p class="prompt" style="top:40px">How does a client feel after working with you?</p>
  <div class="field" style="top:56px;height:51px"></div>
  <p class="prompt" style="top:123px">Why should anyone choose to do business with you over everyone else in your market space? (It could be your experience, your credentials, your philosophy, your empathy, your directness…)</p>
  <div class="field" style="top:151px;height:51px"></div>
  <h3 class="subhead" style="top:220px">Your Value:</h3>
  <p class="prompt" style="top:234px">From the answers above, choose 2 – 3 sentences that stand out most to you and write them below in a way that unifies them.</p>
  <div class="field" style="top:259px;height:35px"></div>
  <div class="field" style="top:298px;height:36px"></div>
  <div class="field" style="top:338px;height:35px"></div>
  <p class="folio">PAGE X OF XX</p>
</section>

<section class="page page--client-intro">
  <div class="section-badge">3</div>
  <h2 class="section-title">Your Ideal Client</h2>
  <p class="lead" style="top:93px">The client for whom you absolutely know you can serve at the highest level, and positively impact.</p>
  <p class="body-copy" style="top:134px">Your ideal clients must recognize themselves in you if you want to capture their interest. Creating avatars of your ideal client(s), helps you to create fictional people with real needs and personalities. This is an in-depth process of researching and understanding who you’re speaking to learn everything about them. Once you know their language, you can begin to speak it. And then they will listen.</p>
  <p class="body-copy" style="top:191px">A lot more work goes into discovering your ideal client. This is only a fraction of it, to help you communicate in a way that resonates with them. But don’t assume that because you’ve done this, you have completely identified your ideal client.</p>
  <div class="profile-table" style="top:247px;grid-template-rows:26px 27px 25px 25px">
    <div class="blank"></div><div class="head">Your Client</div><div class="head">Value That Align</div>
    <div class="label">Male/female/either</div><div class="cell"></div><div class="cell"></div>
    <div class="label">Age range</div><div class="cell"></div><div class="cell"></div>
    <div class="label">Education level</div><div class="cell"></div><div class="cell"></div>
  </div>
  <p class="folio">PAGE X OF XX</p>
</section>

<section class="page page--client-detail">
  <div class="profile-table" style="top:46px;grid-template-rows:25px 29px 25px 33px 24px 36px 32px">
    <div class="blank"></div><div class="head">Your Client</div><div class="head">Value That Align</div>
    <div class="label">Income level</div><div class="cell"></div><div class="cell"></div>
    <div class="label">Biggest aspiration</div><div class="cell"></div><div class="cell"></div>
    <div class="label"><span>Where do they live?</span><span>Urban, Suburban, or Rural?</span></div><div class="cell"></div><div class="cell"></div>
    <div class="label">What do they really want to be like?</div><div class="cell"></div><div class="cell"></div>
    <div class="label"><span>What core values</span><span>do your ideal clients have?</span></div><div class="cell"></div><div class="cell"></div>
    <div class="label"><span>What strong opinions</span><span>do your ideal clients have?</span></div><div class="cell"></div><div class="cell"></div>
  </div>
  <p class="prompt" style="top:282px">Now, from the above, choose 3 words that stand out most about your ideal client. <span class="upright">(For example, are they about youthful energy, fun, and social; urban, hip, techy; conservative, professional, and intellectual… )</span></p>
  <div class="word-boxes"><span></span><span></span><span></span></div>
  <p class="folio">PAGE X OF XX</p>
</section>

</body>
</html>
```